Open House 2017

We need a flyer for an insert for a newspaper for an open house that we are going to have and we are also wanting to list the front of the flyer the 3 pictures of our real estate agents and our Logo.

For the real estate agents : The one with Purple shirt would be the middle picture.

Attached also is our current Logo, Please re-design our Logo a bit to make it look better.

Target Market(s)

Residential and commercial and Land In our rural areas.

Industry/Entity Type

House

Requirements
Must have
• Front page -
• Our logo at the top our 3 pictures at the top after our logo and business address.
• Middle of page Some thing worded similar to the following:"let us place a SOLD sign in your front yard". Or
• " Sold vs. For Sale which would you like to see in your front yard?"
• Our colors for our agency are Gold and Black (the whole flyer does not need to be this color though)
• Join us for an open house in our office
• Wednesday March 1
• 3-6pm
• Back page of flyer: "If you would like to add your name to the Sold Properties list, give us a call today!
• Sold listings which we will get sent to you will also be listed on the back page.
Should not have
• do not make the flyer too "busy" with too many pictures and wording.

```html
<!DOCTYPE html>
<html lang="en">
<head>
<meta charset="utf-8">
<title>Marlow Realty – Open House Flyer</title>
<link href="https://fonts.googleapis.com/css2?family=Cinzel:wght@400;700&family=Crimson+Text:wght@700&family=Roboto+Condensed:wght@400;500&family=Open+Sans:wght@400;700&display=swap" rel="stylesheet">
<style>
:root{
  --gold:#f2b73c;
  --gold-text:#e8b64a;
  --black:#1b1b1b;
  --paper:#ffffff;
  --card-bg:#f3f4f4;
  --ink:#222222;
  --stage:#e4e2df;
}
*{margin:0;padding:0;box-sizing:border-box}
html,body{width:1200px;height:771px;overflow:hidden;background:var(--stage)}
.flyer{position:absolute;top:66px;width:496px;height:636px;overflow:hidden;background:var(--paper);box-shadow:0 4px 14px rgba(0,0,0,.25)}
.front{left:74px}
.back{left:630px;background:var(--card-bg)}

/* front */
.hero-photo{position:absolute;left:0;top:0;width:496px;height:245px;background:linear-gradient(180deg,#8fb3d6 0%,#c9d6df 40%,#e6e2d8 62%,#7d9a55 100%)}
.front-panel{position:absolute;left:0;top:245px;width:496px;height:341px;background:radial-gradient(ellipse at 50% 45%,#4a4a4a 0%,#2c2c2c 55%,#1a1a1a 100%)}
.brand-name{position:absolute;left:0;width:100%;text-align:center;font-family:"Open Sans",sans-serif;font-weight:700;color:var(--gold-text);font-size:22px;line-height:1}
.front .brand-name{top:17px}
.invite{position:absolute;top:70px;left:56px;right:56px;display:flex;align-items:center;gap:6px;font-family:"Cinzel",serif;color:var(--gold-text);font-size:12px;white-space:nowrap}
.invite::before,.invite::after{content:"";flex:1;height:1px;background:var(--gold-text)}
.headline{position:absolute;top:84px;left:0;width:100%;text-align:center;font-family:"Cinzel",serif;font-weight:400;color:#fff;font-size:60px;line-height:1;letter-spacing:1px}
.date-bar{position:absolute;top:142px;left:78px;width:346px;height:33px;background:var(--gold);display:flex;align-items:center;justify-content:center;font-family:"Roboto Condensed",sans-serif;font-weight:500;font-size:21px;color:var(--black)}
.contact-line{position:absolute;top:184px;left:0;width:100%;text-align:center;font-family:"Roboto Condensed",sans-serif;font-size:12px;color:#e6e6e6}
.agent{position:absolute;top:214px;width:106px;height:106px;border-radius:50%;border:3px solid #e8e8e8;background:radial-gradient(circle at 50% 40%,#d8d8d8,#9a9a9a)}
.agent-1{left:44px}.agent-2{left:197px}.agent-3{left:346px}
.slogan-band{position:absolute;left:0;top:586px;width:496px;height:50px;background:var(--gold);display:flex;align-items:center;justify-content:center;font-family:"Crimson Text",serif;font-weight:700;font-size:25px;color:var(--black)}

/* back */
.call-box{position:absolute;left:0;top:0;width:290px;height:130px;background:var(--gold);padding:33px 8px 0 16px;font-family:"Cinzel",serif;font-size:14px;line-height:24px;color:var(--black);white-space:nowrap}
.call-box strong{font-weight:700}
.side-photo{position:absolute;left:292px;top:0;width:204px;height:130px;background:linear-gradient(180deg,#7fa9d3 0%,#c7d2da 45%,#e3e0d6 65%,#6f9350 100%)}
.brand-bar{position:absolute;left:0;top:130px;width:290px;height:64px;background:linear-gradient(90deg,#2c2c2c,#161616)}
.back .brand-name{top:21px}
.phone-box{position:absolute;left:292px;top:130px;width:204px;height:64px;background:var(--gold);display:flex;align-items:center;justify-content:center;gap:8px;font-family:"Open Sans",sans-serif;font-size:18px;color:var(--black)}
.stripes{position:absolute;left:8px;top:206px;width:482px;height:14px;background:repeating-linear-gradient(-45deg,#d8dada 0 3px,transparent 3px 7px)}
.listing{position:absolute;width:113px}
.listing-photo{position:relative;width:113px;height:74px;background:linear-gradient(180deg,#5f8a4c 0%,#a89a84 40%,#7a6a58 75%,#9b9a94 100%)}
.sold-badge{position:absolute;right:-2px;bottom:-24px;width:36px;height:36px;border-radius:50%;background:var(--gold);display:flex;align-items:center;justify-content:center;font-family:"Open Sans",sans-serif;font-size:10px;color:var(--black)}
.listing-address{margin-top:16px;font-family:"Open Sans",sans-serif;font-size:5.5px;color:var(--ink);display:flex;align-items:center;gap:2px}
.listing-desc{margin-top:4px;font-family:"Open Sans",sans-serif;font-size:4.3px;line-height:6px;color:var(--ink);text-align:justify;height:21px;border-bottom:1px solid var(--gold);padding-bottom:2px;overflow:hidden}
.listing-price{font-family:"Open Sans",sans-serif;font-size:8px;color:var(--ink);text-align:center;padding:5px 0 4px;border-bottom:1px solid var(--gold)}
.back-footer{position:absolute;left:0;top:588px;width:496px;height:48px;background:var(--gold);display:flex;align-items:center;justify-content:center;font-family:"Roboto Condensed",sans-serif;font-size:13px;color:var(--black)}
</style>
</head>
<body>

<section class="flyer front">
  <div class="hero-photo" role="img" aria-label="Two-storey white house with a sold sign on a for sale post in the front yard"></div>
  <div class="front-panel">
    <div class="brand-name">Marlow Realty LLC</div>
    <div class="invite">JOIN US FOR AN OPEN HOUSE IN OUR OFFICE</div>
    <h1 class="headline">OPEN HOUSE</h1>
    <div class="date-bar">WEDNESDAY MARCH 1ST FROM 3-6PM</div>
    <div class="contact-line">48 Harbor Lane Fairview, MN 55990 &nbsp;|&nbsp; (555) 014-2290</div>
    <div class="agent agent-1" role="img" aria-label="Portrait of agent"></div>
    <div class="agent agent-2" role="img" aria-label="Portrait of agent in purple shirt"></div>
    <div class="agent agent-3" role="img" aria-label="Portrait of agent"></div>
  </div>
  <div class="slogan-band">Let us place a SOLD sign in your front yard!</div>
</section>

<section class="flyer back">
  <div class="call-box">IF YOU WOULD LIKE TO ADD YOUR<br>NAME TO THE <strong>SOLD PROPERTIES</strong><br>LIST, GIVE US A CALL TODAY!</div>
  <div class="side-photo" role="img" aria-label="Two-storey white house with double garage"></div>
  <div class="brand-bar">
    <div class="brand-name">Marlow Realty LLC</div>
  </div>
  <div class="phone-box">
    <svg width="18" height="18" viewBox="0 0 24 24" aria-hidden="true"><circle cx="12" cy="12" r="10.5" fill="none" stroke="#1b1b1b" stroke-width="2"/><path d="M8.2 6.5c.5-.4 1.1-.3 1.4.2l1 1.7c.3.5.2 1-.2 1.4l-.7.6c.6 1.4 1.6 2.5 3 3.1l.6-.7c.4-.4 1-.5 1.4-.2l1.7 1c.5.3.6 1 .2 1.4l-.9 1c-.6.6-1.5.8-2.3.5-3.1-1.2-5.4-3.5-6.6-6.6-.3-.8-.1-1.7.5-2.3z" fill="#1b1b1b"/></svg>
    (555) 014-2290
  </div>
  <div class="stripes"></div>

  <article class="listing" style="left:15px;top:236px"><div class="listing-photo" role="img" aria-label="Townhome with stone front and brown garage door"><span class="sold-badge">SOLD</span></div><div class="listing-address"><svg width="4" height="6" viewBox="0 0 4 6"><path d="M2 0a2 2 0 0 1 2 2c0 1.5-2 4-2 4S0 3.5 0 2a2 2 0 0 1 2-2z" fill="#222"/></svg>27 B Maple Court Fairview..</div><p class="listing-desc">Bright three bedroom, two bath home with a large yard and double garage, close to the park and schools.</p><div class="listing-price">$139,000.00</div></article>
  <article class="listing" style="left:133px;top:236px"><div class="listing-photo" role="img" aria-label="Townhome with stone front and brown garage door"><span class="sold-badge">SOLD</span></div><div class="listing-address"><svg width="4" height="6" viewBox="0 0 4 6"><path d="M2 0a2 2 0 0 1 2 2c0 1.5-2 4-2 4S0 3.5 0 2a2 2 0 0 1 2-2z" fill="#222"/></svg>27 B Maple Court Fairview..</div><p class="listing-desc">Bright three bedroom, two bath home with a large yard and double garage, close to the park and schools.</p><div class="listing-price">$139,000.00</div></article>
  <article class="listing" style="left:250px;top:236px"><div class="listing-photo" role="img" aria-label="Townhome with stone front and brown garage door"><span class="sold-badge">SOLD</span></div><div class="listing-address"><svg width="4" height="6" viewBox="0 0 4 6"><path d="M2 0a2 2 0 0 1 2 2c0 1.5-2 4-2 4S0 3.5 0 2a2 2 0 0 1 2-2z" fill="#222"/></svg>27 B Maple Court Fairview..</div><p class="listing-desc">Bright three bedroom, two bath home with a large yard and double garage, close to the park and schools.</p><div class="listing-price">$139,000.00</div></article>
  <article class="listing" style="left:368px;top:236px"><div class="listing-photo" role="img" aria-label="Townhome with stone front and brown garage door"><span class="sold-badge">SOLD</span></div><div class="listing-address"><svg width="4" height="6" viewBox="0 0 4 6"><path d="M2 0a2 2 0 0 1 2 2c0 1.5-2 4-2 4S0 3.5 0 2a2 2 0 0 1 2-2z" fill="#222"/></svg>27 B Maple Court Fairview..</div><p class="listing-desc">Bright three bedroom, two bath home with a large yard and double garage, close to the park and schools.</p><div class="listing-price">$139,000.00</div></article>

  <article class="listing" style="left:15px;top:412px"><div class="listing-photo" role="img" aria-label="Townhome with stone front and brown garage door"><span class="sold-badge">SOLD</span></div><div class="listing-address"><svg width="4" height="6" viewBox="0 0 4 6"><path d="M2 0a2 2 0 0 1 2 2c0 1.5-2 4-2 4S0 3.5 0 2a2 2 0 0 1 2-2z" fill="#222"/></svg>27 B Maple Court Fairview..</div><p class="listing-desc">Bright three bedroom, two bath home with a large yard and double garage, close to the park and schools.</p><div class="listing-price">$139,000.00</div></article>
  <article class="listing" style="left:133px;top:412px"><div class="listing-photo" role="img" aria-label="Townhome with stone front and brown garage door"><span class="sold-badge">SOLD</span></div><div class="listing-address"><svg width="4" height="6" viewBox="0 0 4 6"><path d="M2 0a2 2 0 0 1 2 2c0 1.5-2 4-2 4S0 3.5 0 2a2 2 0 0 1 2-2z" fill="#222"/></svg>27 B Maple Court Fairview..</div><p class="listing-desc">Bright three bedroom, two bath home with a large yard and double garage, close to the park and schools.</p><div class="listing-price">$139,000.00</div></article>
  <article class="listing" style="left:250px;top:412px"><div class="listing-photo" role="img" aria-label="Townhome with stone front and brown garage door"><span class="sold-badge">SOLD</span></div><div class="listing-address"><svg width="4" height="6" viewBox="0 0 4 6"><path d="M2 0a2 2 0 0 1 2 2c0 1.5-2 4-2 4S0 3.5 0 2a2 2 0 0 1 2-2z" fill="#222"/></svg>27 B Maple Court Fairview..</div><p class="listing-desc">Bright three bedroom, two bath home with a large yard and double garage, close to the park and schools.</p><div class="listing-price">$139,000.00</div></article>
  <article class="listing" style="left:368px;top:412px"><div class="listing-photo" role="img" aria-label="Townhome with stone front and brown garage door"><span class="sold-badge">SOLD</span></div><div class="listing-address"><svg width="4" height="6" viewBox="0 0 4 6"><path d="M2 0a2 2 0 0 1 2 2c0 1.5-2 4-2 4S0 3.5 0 2a2 2 0 0 1 2-2z" fill="#222"/></svg>27 B Maple Court Fairview..</div><p class="listing-desc">Bright three bedroom, two bath home with a large yard and double garage, close to the park and schools.</p><div class="listing-price">$139,000.00</div></article>

  <footer class="back-footer">48 Harbor Lane Fairview, MN 55990 &nbsp;|&nbsp; (555) 014-2290 &nbsp;|&nbsp; www.marlowrealty.com</footer>
</section>

</body>
</html>
```